Flyer design for guitar parts website

We are looking for an eye catching flyer design to include within our order packaging to persuade our Zubit and Kestrix customers to purchase from our website.

The flyer will be double sided, with one side offering buyers a discount for shopping on our website, and the other side advertising our loyalty points scheme, and the benefits the company it.

We've attached our company logo and our loyalty points logo.

I've also attached a banner design we used recently for our rewards program.

Target Market(s)

Males, aged 20 to 65

Colors
f68e4d
f04a51
886aae
3377b5

Requirements
Must have
• The flyer will be A6 size
• The focus of the front must be on the 20% discount for first order.
• The web address must also be prominent, as must our logo
• There will also be a discount code displayed.
• The back fo the flyer will contain the loyalyt points logo, and information about how the points work, and how they can be redeemed

```html
<!DOCTYPE html>
<html lang="en">
<head>
<meta charset="utf-8">
<title>Ridgeline Guitars – Flyer</title>
<link rel="stylesheet" href="https://fonts.googleapis.com/css2?family=Open+Sans:wght@400;600;700;800&display=swap">
<style>
  :root{
    --stage:#b6c8c2;
    --red:#d3262c;
    --red-deep:#b81d2a;
    --navy:#2c2f8f;
    --charcoal:#333336;
    --yellow:#f2c21b;
    --white:#ffffff;
    --ink:#111111;
  }
  *{box-sizing:border-box;margin:0;padding:0}
  html,body{width:1200px;height:721px;overflow:hidden}
  body{background:var(--stage);font-family:"Open Sans",Arial,sans-serif;position:relative}

  .flyer{position:absolute;top:52px;width:436px;height:617px;overflow:hidden;box-shadow:0 6px 18px rgba(0,0,0,.25)}
  .flyer--front{left:150px;background:linear-gradient(180deg,var(--red) 0%,var(--red) 45%,#3a1e3e 72%,var(--navy) 100%)}
  .flyer--back{left:614px;background:linear-gradient(180deg,var(--red) 0%,var(--red) 34%,var(--charcoal) 60%,var(--charcoal) 100%)}

  /* front */
  .guitar-photo{position:absolute;left:0;top:110px;width:436px;height:420px;
    background:radial-gradient(ellipse at 45% 65%,#1a1a22 0%,#3b2240 45%,rgba(60,20,50,0) 75%),
               linear-gradient(160deg,rgba(255,255,255,.0) 40%,rgba(255,255,255,.08) 60%,rgba(0,0,0,0) 80%)}
  .brand{position:absolute;left:26px;top:34px;color:var(--white);font-weight:800;line-height:1}
  .brand__small{display:block;font-size:30px;letter-spacing:1px;text-transform:lowercase}
  .brand__large{display:block;font-size:58px;letter-spacing:2px}
  .brand__tld{font-size:14px;margin-left:4px}
  .badge{position:absolute;left:22px;top:160px;width:200px;height:120px}
  .badge svg{position:absolute;inset:0}
  .badge__text{position:absolute;inset:0;display:flex;flex-direction:column;align-items:center;justify-content:center;color:var(--ink);font-weight:800;transform:rotate(-8deg)}
  .badge__big{font-size:30px;line-height:1}
  .badge__small{font-size:11px;margin-top:2px}
  .code{position:absolute;right:22px;bottom:90px;border:2px dashed var(--white);padding:4px 10px;text-align:center;color:var(--white);font-weight:800;background:rgba(0,0,0,.25)}
  .code__label{display:block;font-size:11px;letter-spacing:1px}
  .code__value{display:block;font-size:22px;letter-spacing:3px}
  .front-url{position:absolute;left:0;right:0;bottom:28px;text-align:center;color:var(--white);font-weight:800;font-size:24px;text-shadow:0 2px 3px rgba(0,0,0,.5)}

  /* back */
  .rewards-logo{position:absolute;left:0;right:0;top:36px;text-align:center;color:var(--yellow);font-weight:800;line-height:1}
  .rewards-logo__mark{display:inline-block;width:18px;height:18px;background:var(--yellow);vertical-align:middle;margin-right:10px}
  .rewards-logo__name{font-size:40px;vertical-align:middle}
  .intro{position:absolute;left:30px;right:30px;top:104px;text-align:center;color:var(--white);font-weight:700;font-size:13px;line-height:1.35;text-transform:uppercase}
  .col{position:absolute;top:160px;color:var(--ink)}
  .col--earn{left:30px;width:210px}
  .col--spend{left:250px;width:170px}
  .col__title{font-size:16px;font-weight:800;color:var(--white);text-transform:uppercase;margin-bottom:12px;display:flex;align-items:center;gap:8px}
  .item{display:flex;align-items:center;gap:10px;margin-bottom:12px}
  .item__icon{flex:none;width:26px;height:26px}
  .item__text{font-size:11px;font-weight:700;line-height:1.25;color:var(--white)}
  .col--earn .item__text,.col--spend .item__text{color:var(--white)}
  .item__text span{display:block;font-weight:600}
  .cta{position:absolute;left:0;right:0;bottom:40px;text-align:center;color:var(--white);font-weight:800}
  .cta__line{font-size:15px;text-transform:uppercase;margin-bottom:8px}
  .cta__url{font-size:24px}
</style>
</head>
<body>

<section class="flyer flyer--front" aria-label="Front: first order discount">
  <div class="guitar-photo" role="img" aria-label="Photo of a black single-cut electric guitar with a white fretboard, lit in red and blue"></div>
  <div class="brand">
    <span class="brand__small">ridgeline</span>
    <span class="brand__large">GUITARS<span class="brand__tld">.CO.UK</span></span>
  </div>
  <div class="badge">
    <svg viewBox="0 0 200 120" aria-hidden="true">
      <polygon fill="var(--yellow)" points="100,4 116,22 140,8 146,30 174,24 168,46 196,52 176,68 196,86 168,88 172,112 146,102 134,118 112,104 92,118 80,100 56,114 54,92 26,98 34,76 6,66 30,52 12,34 40,32 40,8 64,22 82,4"/>
    </svg>
    <div class="badge__text">
      <span class="badge__big">20% OFF</span>
      <span class="badge__small">ON YOUR FIRST ORDER</span>
    </div>
  </div>
  <div class="code">
    <span class="code__label">DISCOUNT CODE</span>
    <span class="code__value">XXXXXX</span>
  </div>
  <p class="front-url">WWW.RIDGELINEGUITARS.CO.UK</p>
</section>

<section class="flyer flyer--back" aria-label="Back: loyalty points scheme">
  <div class="rewards-logo"><span class="rewards-logo__mark"></span><span class="rewards-logo__name">ENCORE REWARDS</span></div>
  <p class="intro">Earn Encore Points for different actions, and turn those Encore Points into awesome rewards!</p>

  <div class="col col--earn">
    <h2 class="col__title">Ways to earn
      <svg width="22" height="20" viewBox="0 0 22 20" aria-hidden="true"><circle cx="11" cy="5" r="4" fill="var(--ink)"/><path d="M2 14 q9 8 18 0" stroke="var(--ink)" stroke-width="2.5" fill="none"/></svg>
    </h2>
    <div class="item"><svg class="item__icon" viewBox="0 0 26 26"><circle cx="13" cy="13" r="10" fill="var(--ink)"/></svg><p class="item__text">Like on Chatterly<span>50 Encore Points</span></p></div>
    <div class="item"><svg class="item__icon" viewBox="0 0 26 26"><circle cx="13" cy="13" r="10" fill="var(--ink)"/></svg><p class="item__text">Share on Chatterly<span>50 Encore Points</span></p></div>
    <div class="item"><svg class="item__icon" viewBox="0 0 26 26"><circle cx="13" cy="13" r="10" fill="var(--ink)"/></svg><p class="item__text">Follow us on Snapframe<span>50 Encore Points</span></p></div>
    <div class="item"><svg class="item__icon" viewBox="0 0 26 26"><circle cx="13" cy="13" r="10" fill="var(--ink)"/></svg><p class="item__text">Share on Chirpline<span>50 Encore Points</span></p></div>
    <div class="item"><svg class="item__icon" viewBox="0 0 26 26"><circle cx="13" cy="13" r="10" fill="var(--ink)"/></svg><p class="item__text">Follow on Chirpline<span>50 Encore Points</span></p></div>
    <div class="item"><svg class="item__icon" viewBox="0 0 26 26"><rect x="3" y="4" width="20" height="6" fill="none" stroke="var(--ink)" stroke-width="2"/><rect x="5" y="10" width="16" height="12" fill="none" stroke="var(--ink)" stroke-width="2"/></svg><p class="item__text">Signup Bonus<span>200 Encore Points</span></p></div>
  </div>

  <div class="col col--spend">
    <h2 class="col__title">Ways to spend
      <svg width="22" height="20" viewBox="0 0 22 20" aria-hidden="true"><rect x="2" y="7" width="18" height="12" fill="none" stroke="var(--ink)" stroke-width="2"/><rect x="1" y="4" width="20" height="4" fill="var(--ink)"/><line x1="11" y1="4" x2="11" y2="19" stroke="var(--ink)" stroke-width="2"/></svg>
    </h2>
    <div class="item"><svg class="item__icon" viewBox="0 0 26 26"><rect x="2" y="7" width="22" height="13" fill="none" stroke="var(--ink)" stroke-width="2"/><circle cx="13" cy="13.5" r="3" fill="none" stroke="var(--ink)" stroke-width="2"/></svg><p class="item__text">£5 off coupon<span>500 Encore Points</span></p></div>
    <div class="item"><svg class="item__icon" viewBox="0 0 26 26"><rect x="2" y="7" width="22" height="13" fill="none" stroke="var(--ink)" stroke-width="2"/><circle cx="13" cy="13.5" r="3" fill="none" stroke="var(--ink)" stroke-width="2"/></svg><p class="item__text">£10 off coupon<span>1000 Encore Points</span></p></div>
    <div class="item"><svg class="item__icon" viewBox="0 0 26 26"><rect x="2" y="7" width="22" height="13" fill="none" stroke="var(--ink)" stroke-width="2"/><circle cx="13" cy="13.5" r="3" fill="none" stroke="var(--ink)" stroke-width="2"/></svg><p class="item__text">£25 off coupon<span>2500 Encore Points</span></p></div>
  </div>

  <div class="cta">
    <p class="cta__line">Visit our website and become a member today!</p>
    <p class="cta__url">WWW.RIDGELINEGUITARS.CO.UK</p>
  </div>
</section>

</body>
</html>
```